Elegant Gather Glow Rentals DL flyer

We run a Gather Glow Rentals business - this will be used as a business card as well.

our website is gatherglowrentals.com.au

Front page it sour logo which is attached website details - on the front it needs to say wedding and event hire needs etc..

on the back we will have a spot for 4 products but we want to say there is more so check our the website

A background in the flyer only for example like this would be good http://backdropvista.com/black-background-wallpaper_2881.html

Wedding

• nice background elegant in style pink and black is the colours

```html
<!DOCTYPE html>
<html lang="en">
<head>
<meta charset="utf-8">
<title>Gather Glow Rentals – Business Card</title>
<link rel="stylesheet" href="https://fonts.googleapis.com/css2?family=Great+Vibes&family=Exo+2:wght@300;400&display=swap">
<style>
  :root{
    --pink:#d6168c;
    --pink-soft:#e0409f;
    --ink-deep:#1c1c1e;
    --silver:#e6e6e6;
    --grey-text:#5a5a5a;
    --panel:#f1f1f1;
    --stage-top:#3a3a3a;
    --stage-bottom:#1e1e1e;
  }
  *{margin:0;padding:0;box-sizing:border-box}
  html,body{width:1200px;height:658px;overflow:hidden}
  body{
    background:linear-gradient(180deg,var(--stage-top),var(--stage-bottom));
    position:relative;
    font-family:"Exo 2",sans-serif;
  }
  .card{
    position:absolute;top:196px;width:424px;height:290px;
    overflow:hidden;box-shadow:0 10px 30px rgba(0,0,0,.5);
  }
  .card-bg{
    position:absolute;inset:0;
    background:radial-gradient(ellipse at 50% 40%,#3a3a3c,var(--ink-deep));
  }
  .card-front{left:166px}
  .card-back{left:610px}

  /* front */
  .front-content{position:relative;height:100%;display:flex;flex-direction:column;align-items:center}
  .brand-dot{width:80px;height:80px;border-radius:50%;background:var(--pink);margin-top:30px}
  .brand-name{
    font-family:"Great Vibes",cursive;font-size:40px;color:var(--silver);
    margin-top:6px;line-height:1.05;font-weight:400;
  }
  .tagline{
    font-family:"Great Vibes",cursive;font-size:22px;color:var(--pink);line-height:1;
  }
  .contact{margin-top:12px;display:flex;flex-direction:column;align-items:center;gap:6px}
  .contact-row{display:flex;align-items:center;gap:8px;color:#fff;font-weight:300}
  .contact-row.phone{font-size:22px}
  .contact-row.email{font-size:20px}
  .icon-box{width:26px;height:26px;background:var(--pink);border-radius:4px;display:flex;align-items:center;justify-content:center}

  /* back */
  .back-content{position:relative;height:100%;display:flex;flex-direction:column}
  .back-header{height:50px;display:flex;align-items:center;justify-content:center;gap:10px}
  .back-header .brand-dot{width:32px;height:32px;margin:0}
  .header-text{display:flex;flex-direction:column;align-items:center}
  .back-header .brand-name{font-size:22px;margin:0}
  .back-header .tagline{font-size:13px}
  .pink-rule{height:5px;background:var(--pink)}
  .products{
    background:var(--panel);height:170px;position:relative;
    display:grid;grid-template-columns:1fr 1fr;grid-template-rows:1fr 1fr;
  }
  .products::before{content:"";position:absolute;left:50%;top:8px;bottom:10px;width:2px;background:var(--pink)}
  .products::after{content:"";position:absolute;left:14px;right:8px;top:50%;height:2px;background:var(--pink)}
  .product{padding:9px 10px 0 28px}
  .product-tag{
    display:inline-block;background:var(--pink);color:#fff;border-radius:3px;
    font-family:"Great Vibes",cursive;font-size:15px;padding:0 8px;line-height:18px;
    box-shadow:0 1px 2px rgba(0,0,0,.3);
  }
  .product-desc{
    margin-top:4px;display:grid;grid-template-columns:repeat(3,max-content);column-gap:4px;
    font-size:6px;line-height:7px;color:var(--grey-text);
  }
  .back-footer{flex:1;display:flex;align-items:center;justify-content:center;gap:6px}
  .footer-lead{color:var(--pink-soft);font-size:11px}
  .footer-url{color:var(--silver);font-size:20px;font-weight:300}
</style>
</head>
<body>

<section class="card card-front">
  <div class="card-bg" role="img" aria-label="Dark charcoal damask wallpaper pattern"></div>
  <div class="front-content">
    <div class="brand-dot"></div>
    <h1 class="brand-name">Gather Glow Rentals</h1>
    <p class="tagline">for all your wedding &amp; event hire needs</p>
    <div class="contact">
      <p class="contact-row phone">
        <span class="icon-box">
          <svg width="16" height="16" viewBox="0 0 24 24"><path fill="#fff" d="M6.6 10.8a15 15 0 0 0 6.6 6.6l2.2-2.2c.3-.3.7-.4 1-.2 1.1.4 2.3.6 3.6.6.6 0 1 .4 1 1V20c0 .6-.4 1-1 1A17 17 0 0 1 3 4c0-.6.4-1 1-1h3.5c.6 0 1 .4 1 1 0 1.3.2 2.5.6 3.6.1.3 0 .7-.2 1z"/></svg>
        </span>
        0412555019
      </p>
      <p class="contact-row email">
        <span class="icon-box">
          <svg width="16" height="12" viewBox="0 0 16 12"><rect x="0.5" y="0.5" width="15" height="11" fill="none" stroke="#fff"/><path d="M1 1l7 6 7-6" fill="none" stroke="#fff"/></svg>
        </span>
        info@gatherglowrentals.com.au
      </p>
    </div>
  </div>
</section>

<section class="card card-back">
  <div class="card-bg" role="img" aria-label="Dark charcoal damask wallpaper pattern"></div>
  <div class="back-content">
    <header class="back-header">
      <div class="brand-dot"></div>
      <div class="header-text">
        <h2 class="brand-name">Gather Glow Rentals</h2>
        <p class="tagline">wedding &amp; event hire</p>
      </div>
    </header>
    <div class="pink-rule"></div>
    <div class="products">
      <article class="product">
        <span class="product-tag">Product</span>
        <div class="product-desc">
          <span>Product description</span><span>Product description</span><span>Product description</span>
          <span>Product description</span><span>Product description</span><span>Product description</span>
          <span>Product description</span><span>Product description</span><span>Product description</span>
          <span>Product description</span><span>Product description</span><span>Product description</span>
          <span>Product description</span><span>Product description</span><span>Product description</span>
          <span>Product description</span><span>Product description</span><span>Product description</span>
        </div>
      </article>
      <article class="product">
        <span class="product-tag">Product</span>
        <div class="product-desc">
          <span>Product description</span><span>Product description</span><span>Product description</span>
          <span>Product description</span><span>Product description</span><span>Product description</span>
          <span>Product description</span><span>Product description</span><span>Product description</span>
          <span>Product description</span><span>Product description</span><span>Product description</span>
          <span>Product description</span><span>Product description</span><span>Product description</span>
          <span>Product description</span><span>Product description</span><span>Product description</span>
        </div>
      </article>
      <article class="product">
        <span class="product-tag">Product</span>
        <div class="product-desc">
          <span>Product description</span><span>Product description</span><span>Product description</span>
          <span>Product description</span><span>Product description</span><span>Product description</span>
          <span>Product description</span><span>Product description</span><span>Product description</span>
          <span>Product description</span><span>Product description</span><span>Product description</span>
          <span>Product description</span><span>Product description</span><span>Product description</span>
          <span>Product description</span><span>Product description</span><span>Product description</span>
        </div>
      </article>
      <article class="product">
        <span class="product-tag">Product</span>
        <div class="product-desc">
          <span>Product description</span><span>Product description</span><span>Product description</span>
          <span>Product description</span><span>Product description</span><span>Product description</span>
          <span>Product description</span><span>Product description</span><span>Product description</span>
          <span>Product description</span><span>Product description</span><span>Product description</span>
          <span>Product description</span><span>Product description</span><span>Product description</span>
          <span>Product description</span><span>Product description</span><span>Product description</span>
        </div>
      </article>
    </div>
    <footer class="back-footer">
      <span class="footer-lead">Check more at:</span>
      <span class="footer-url">gatherglowrentals.com.au</span>
    </footer>
  </div>
</section>

</body>
</html>
```